Adventurous female pilot

I am looking for a personal business card, for a very well qualified female pilot, with a lot of aviation experience.

Currently an airline pilot, have worked as a bush pilot in Africa, looking to get into corporate aviation, or private jet owners.
Want a classy looking card for networking...

Could be interested in a retro\vintage look also?!

An idea,, is an african sunset background, with my wings\logo on it
Updates

I just want to say thank you to all of your for your amazing designs!

I have been very busy flying this past week , so not had a chance to be on the computer much.
But I provide some feedback, and conclusions very soon!
Thank you again.

Marla

Reason: Still waiting on a couple of revisions to be 100% about my choice!

Target Market(s)

corporate aviation, private jet owners, casino's,
General audience.
networking

Industry/Entity Type

Airline

Requirements
Nice to have
• Classy, edgy, sexy, but also feminine

```html
<!DOCTYPE html>
<html lang="en">
<head>
<meta charset="utf-8">
<title>Marla Rowan Aviation – Business Card</title>
<link rel="stylesheet" href="https://fonts.googleapis.com/css2?family=Montserrat:wght@300;400;600&family=Open+Sans:wght@400;600&display=swap">
<style>
  :root {
    --page-bg: #3b2016;
    --card-yellow: #f4ec9c;
    --card-yellow-deep: #e7d36e;
    --brand-white: #fbfbf9;
    --band-red: #f2262e;
    --band-red-dark: #d31820;
    --ink-grey: #5a5a5a;
    --contact-red: #e2312a;
    --icon-grey: #8a8a8a;
    --sunset-top: #fbe7a6;
    --sunset-mid: #f5b25a;
    --sunset-low: #d98a3a;
  }
  * { box-sizing: border-box; margin: 0; padding: 0; }
  html, body { width: 1200px; height: 900px; overflow: hidden; }
  body {
    background: var(--page-bg);
    display: flex; align-items: center; justify-content: center;
    font-family: "Open Sans", Arial, sans-serif;
  }
  .card {
    position: relative;
    width: 1000px; height: 580px;
    background: linear-gradient(160deg, var(--card-yellow), var(--card-yellow-deep));
    border-radius: 6px;
    overflow: hidden;
    box-shadow: 0 18px 40px rgba(0,0,0,.45);
  }
  .brand-panel {
    position: absolute; left: 0; top: 0; bottom: 0; width: 420px;
    background: var(--brand-white);
    border-bottom-right-radius: 220px;
    display: flex; flex-direction: column; align-items: center; justify-content: center;
    padding-right: 50px; padding-bottom: 40px;
    z-index: 2;
  }
  .brand-mark {
    width: 70px; height: 70px; border-radius: 50%;
    border: 2px solid var(--ink-grey);
    margin-bottom: 26px;
  }
  .brand-name {
    font-family: "Montserrat", Arial, sans-serif;
    font-weight: 400; font-size: 38px; letter-spacing: 3px;
    color: var(--ink-grey); white-space: nowrap;
  }
  .brand-tagline {
    font-family: "Montserrat", Arial, sans-serif;
    font-weight: 400; font-size: 15px; letter-spacing: 4px;
    color: var(--ink-grey); margin-top: 6px;
  }
  .red-frame {
    position: absolute; left: 400px; top: 0; right: 0; height: 450px;
    background: linear-gradient(180deg, var(--band-red), var(--band-red-dark));
    border-bottom-left-radius: 90px;
  }
  .scene-window {
    position: absolute; left: 36px; top: 0; right: 0; bottom: 36px;
    border-bottom-left-radius: 62px;
    overflow: hidden;
    background: linear-gradient(180deg, var(--sunset-top) 0%, var(--sunset-mid) 55%, var(--sunset-low) 100%);
  }
  .pilot-portrait {
    position: absolute; right: 50px; top: 70px; bottom: 0; width: 300px;
    border-radius: 150px 150px 0 0;
    background: linear-gradient(180deg, #8a5a3c 0%, #6d6d6d 60%, #4b4b4b 100%);
    opacity: .85;
  }
  .red-edge {
    position: absolute; left: 0; right: 0; bottom: 0; height: 10px;
    background: var(--band-red);
  }
  .contacts {
    position: absolute; left: 440px; top: 466px;
    list-style: none;
    z-index: 3;
  }
  .contacts li {
    display: flex; align-items: center; gap: 10px;
    font-size: 15px; color: var(--contact-red); line-height: 28px;
    white-space: nowrap;
  }
  .contacts .label { font-weight: 600; }
  .contacts svg { width: 18px; height: 18px; flex: none; }
</style>
</head>
<body>
  <div class="card">
    <div class="red-frame">
      <div class="scene-window" role="img" aria-label="African savanna sunset with silhouettes of elephants, giraffes and acacia trees">
        <div class="pilot-portrait" role="img" aria-label="Illustration of a female pilot with long brown hair and sunglasses"></div>
      </div>
    </div>

    <div class="brand-panel">
      <div class="brand-mark"></div>
      <div class="brand-name">MARLA ROWAN</div>
      <div class="brand-tagline">AVIATION</div>
    </div>

    <ul class="contacts">
      <li>
        <svg viewBox="0 0 18 18"><circle cx="9" cy="9" r="9" fill="var(--icon-grey)"/><rect x="4.5" y="6" width="9" height="6" fill="none" stroke="#fff" stroke-width="1.2"/><path d="M4.5 6 L9 9.5 L13.5 6" fill="none" stroke="#fff" stroke-width="1.2"/></svg>
        <span><span class="label">E-Mail :</span> marlarowan@skymail.net</span>
      </li>
      <li>
        <svg viewBox="0 0 18 18"><circle cx="9" cy="9" r="9" fill="var(--icon-grey)"/><rect x="6.3" y="4" width="5.4" height="10" rx="1" fill="none" stroke="#fff" stroke-width="1.2"/><circle cx="9" cy="12" r=".7" fill="#fff"/></svg>
        <span><span class="label">Cell Taipei :</span> +886 970-555-014</span>
      </li>
      <li>
        <svg viewBox="0 0 18 18"><circle cx="9" cy="9" r="9" fill="var(--icon-grey)"/><path d="M6 4.5 L7.8 4.5 L8.5 7 L7.4 8 Q8.3 10 10 10.6 L11 9.5 L13.5 10.2 L13.5 12 Q13 13.5 11.5 13.3 Q5 12 4.7 6 Q4.6 4.6 6 4.5 Z" fill="#fff"/></svg>
        <span><span class="label">Cell US :</span> +1 702-555-0187</span>
      </li>
    </ul>

    <div class="red-edge"></div>
  </div>
</body>
</html>
```